Flyer für Vermietung von Baumaschinen und Werkzeugen
Zielgruppe
Vermietung von Baumaschinen und Werkzeugen, sowie der Verkauf von Baustoffen /-materialien
Aufgabenstellung
Ich hätte gerne einen Flyer in Din A5 oder Din A6. Auf einer Seite soll Werbung für die Vermietung gemacht werden, auf der anderen Werbung für den Verkauf.
Das Logo zur Einbindung wird nachgeliefert.
Es soll ein Vermerk auf den Flyer, 'Jetzt neu bei Heidelberg-Leimen'
Auch soll die Adresse mit auf den flyer: www.kraglund.de
Als Farbe bitte grüntöne verwenden

```html
<!DOCTYPE html>
<html lang="de">
<head>
<meta charset="utf-8">
<title>Baustoffhandel – Kraglund</title>
<link rel="stylesheet" href="https://fonts.googleapis.com/css2?family=Baloo+2:wght@500;600&family=Bungee&family=Bungee+Inline&family=Lilita+One&display=swap">
<style>
  :root{
    --green:#2d8a57;
    --green-dark:#1f6e43;
    --green-light:#57c48a;
    --text-green:#1f7a45;
    --navy:#262d38;
    --white:#ffffff;
    --photo-a:#7a3f28;
    --photo-b:#c0673f;
    --photo-c:#8e8a80;
  }
  *{margin:0;padding:0;box-sizing:border-box}
  html,body{width:849px;height:1200px;overflow:hidden;background:var(--white)}
  .flyer{position:relative;width:849px;height:1200px;background:var(--white);font-family:"Baloo 2",sans-serif;color:var(--text-green)}
  .hero{position:absolute;left:0;top:0;width:849px;height:660px}
  .title{position:absolute;left:432px;top:22px;font-family:"Bungee Inline",sans-serif;font-size:40px;color:var(--green);letter-spacing:0.5px;line-height:1}
  .logo-badge{position:absolute;left:37px;top:36px;width:188px;height:188px;border-radius:50%;background:var(--navy);display:flex;align-items:center;justify-content:center;color:var(--white);font-family:"Lilita One",sans-serif;font-size:22px;letter-spacing:1px}
  .badge-new{position:absolute;left:100px;top:500px;font-family:"Lilita One",sans-serif;font-size:50px;color:var(--white);transform:rotate(-5deg);transform-origin:left top;letter-spacing:1px;line-height:1}
  .badge-where{position:absolute;left:124px;top:575px;width:220px;font-family:"Lilita One",sans-serif;font-size:19px;color:var(--white);text-align:center;transform:rotate(-5deg);line-height:1.1}
  .why{position:absolute;left:43px;top:675px;font-family:"Bungee Inline",sans-serif;font-size:28px;color:var(--green);line-height:1}
  .benefits{position:absolute;left:43px;top:750px;list-style:none}
  .benefits li{display:flex;align-items:center;height:65px;font-size:18px;font-weight:600;color:var(--text-green)}
  .benefits svg{width:36px;height:36px;margin-right:10px;flex:none}
  .info{position:absolute;left:436px;top:645px;width:368px}
  .info h2{font-family:"Bungee Inline",sans-serif;font-weight:400;font-size:20px;color:var(--green);line-height:1.05}
  .info p{font-size:16.6px;font-weight:500;line-height:20.5px;text-align:justify;margin-bottom:21px;color:var(--text-green)}
  .footer{position:absolute;left:0;top:1094px;width:849px;height:106px;background:var(--green);color:var(--white)}
  .contact{position:absolute;top:8px;font-size:13.5px;line-height:19px;font-weight:500}
  .contact.phone{left:102px;text-align:center}
  .contact.web{left:388px}
  .contact.addr{left:690px;text-align:center}
  .footer .icon{position:absolute;top:16px;width:20px;height:20px}
  .site{position:absolute;left:0;top:60px;width:849px;text-align:center;font-family:"Bungee",sans-serif;font-size:27px;letter-spacing:27px;padding-left:27px;line-height:1}
</style>
</head>
<body>
<div class="flyer">
  <svg class="hero" viewBox="0 0 849 660" aria-hidden="false">
    <defs>
      <linearGradient id="photoTone" x1="0" y1="0" x2="1" y2="1">
        <stop offset="0" stop-color="var(--photo-c)"/>
        <stop offset="0.35" stop-color="var(--photo-b)"/>
        <stop offset="0.7" stop-color="var(--photo-a)"/>
        <stop offset="1" stop-color="#d9661f"/>
      </linearGradient>
    </defs>
    <path role="img" aria-label="Foto: Bauarbeiter mit Schutzhelm und Tablet vor Paletten mit Ziegelsteinen im Lager" d="M0 0 H262 C320 55 380 72 460 78 L849 104 V395 C780 505 650 568 430 572 C260 575 120 520 0 455 Z" fill="url(#photoTone)"/>
    <path d="M0 330 C70 400 140 450 210 495 L185 508 C120 480 50 455 0 445 Z" fill="var(--green-dark)"/>
    <path d="M0 350 C60 405 120 445 170 480 L150 490 C100 465 45 445 0 430 Z" fill="var(--green-light)"/>
    <path d="M300 585 C540 600 720 540 849 390 V430 C720 580 540 635 300 612 Z" fill="var(--green)"/>
    <path d="M340 588 C560 595 720 530 800 450 L806 458 C720 545 560 602 340 592 Z" fill="var(--green-light)"/>
    <polygon points="62,510 398,474 393,555 52,590" fill="var(--green-light)"/>
    <polygon points="118,598 340,562 345,620 125,648" fill="var(--green)"/>
    <polygon points="340,562 364,570 345,620" fill="#7a2c25"/>
    <line x1="160" y1="492" x2="315" y2="470" stroke="#222" stroke-width="1.5"/>
    <line x1="265" y1="557" x2="372" y2="546" stroke="#e8f0a0" stroke-width="1.5"/>
    <line x1="185" y1="633" x2="270" y2="624" stroke="#222" stroke-width="1.5"/>
    <g role="img" aria-label="Illustration: Megafon">
      <ellipse cx="72" cy="605" rx="40" ry="26" fill="#cfd3e0" transform="rotate(-20 72 605)"/>
    </g>
  </svg>

  <h1 class="title">Baustoffhandel</h1>
  <div class="logo-badge">KRAGLUND</div>

  <div class="badge-new">JETZT NEU</div>
  <div class="badge-where">BEI<br>HEIDELBERG-LEIMEN</div>

  <h2 class="why">Warum Kraglund?</h2>
  <ul class="benefits">
    <li><svg viewBox="0 0 36 36"><path d="M30 14 A14 14 0 1 1 24 6" fill="none" stroke="var(--green)" stroke-width="3" stroke-linecap="round"/><path d="M11 17 L17 23 L33 5" fill="none" stroke="var(--green-light)" stroke-width="4" stroke-linecap="round" stroke-linejoin="round"/></svg>Umfangreiches Sortiment</li>
    <li><svg viewBox="0 0 36 36"><path d="M30 14 A14 14 0 1 1 24 6" fill="none" stroke="var(--green)" stroke-width="3" stroke-linecap="round"/><path d="M11 17 L17 23 L33 5" fill="none" stroke="var(--green-light)" stroke-width="4" stroke-linecap="round" stroke-linejoin="round"/></svg>Kompetente Beratung</li>
    <li><svg viewBox="0 0 36 36"><path d="M30 14 A14 14 0 1 1 24 6" fill="none" stroke="var(--green)" stroke-width="3" stroke-linecap="round"/><path d="M11 17 L17 23 L33 5" fill="none" stroke="var(--green-light)" stroke-width="4" stroke-linecap="round" stroke-linejoin="round"/></svg>Verfügbarkeit von Großmengen</li>
    <li><svg viewBox="0 0 36 36"><path d="M30 14 A14 14 0 1 1 24 6" fill="none" stroke="var(--green)" stroke-width="3" stroke-linecap="round"/><path d="M11 17 L17 23 L33 5" fill="none" stroke="var(--green-light)" stroke-width="4" stroke-linecap="round" stroke-linejoin="round"/></svg>Qualitätsprodukte</li>
    <li><svg viewBox="0 0 36 36"><path d="M30 14 A14 14 0 1 1 24 6" fill="none" stroke="var(--green)" stroke-width="3" stroke-linecap="round"/><path d="M11 17 L17 23 L33 5" fill="none" stroke="var(--green-light)" stroke-width="4" stroke-linecap="round" stroke-linejoin="round"/></svg>Lokales Unternehmen</li>
  </ul>

  <section class="info">
    <h2>Vielfältig und komplett</h2>
    <p>Wir verstehen, dass jedes Projekt einzigartig ist, deshalb bieten wir eine breite Palette von Baumaterialien und Baustoffen an, um sicherzustellen, dass Sie genau das finden, was Sie benötigen.</p>
    <h2>Unser Anspruch</h2>
    <p>Bei uns finden Sie nicht nur erstklassige Baumaterialien, sondern auch erstklassige Beratung. Unser Team steht Ihnen zur Seite, um sicherzustellen, dass Sie die optimalen Entscheidungen für Ihr Bauprojekt treffen. Mit unserer kompetenten Beratung sind Sie auf dem besten Weg zum Erfolg.</p>
    <h2>Unsere Preise</h2>
    <p>Wir wissen, dass Kosten eine wichtige Rolle spielen, deshalb bieten wir erstklassige Baumaterialien und Baustoffe zu Preisen, die Ihre Projekte erschwinglich machen.</p>
  </section>

  <footer class="footer">
    <div class="contact phone">+00 000 000 000<br>+00 000 000 000</div>
    <svg class="icon" style="left:340px" viewBox="0 0 20 20"><g fill="none" stroke="#fff" stroke-width="1.4"><circle cx="10" cy="10" r="8"/><ellipse cx="10" cy="10" rx="3.5" ry="8"/><line x1="2" y1="10" x2="18" y2="10"/><line x1="3.5" y1="6" x2="16.5" y2="6"/><line x1="3.5" y1="14" x2="16.5" y2="14"/></g></svg>
    <div class="contact web">www.yourmail@postfach.de<br>www.yourwesite.com</div>
    <svg class="icon" style="left:634px" viewBox="0 0 20 20"><g fill="none" stroke="#fff" stroke-width="1.4"><path d="M10 17 C6 12 5 9.5 5 7.5 A5 5 0 0 1 15 7.5 C15 9.5 14 12 10 17 Z"/><circle cx="10" cy="7.5" r="1.8"/><ellipse cx="10" cy="17.5" rx="5" ry="1.5"/></g></svg>
    <div class="contact addr">Your company<br>address here</div>
    <div class="site">WWW.KRAGLUND.DE</div>
  </footer>
</div>
</body>
</html>
```